Soccer Training for Boys and Girls

I need like a flyer to post on facebook and instagram.
This is what O want to have on it.
you can use any color , soccer field on the background , or any soccer pictures.
Recreational and Travel Teams
Ages :5 to 14 years old
Field: Holloway Fenwick Middle School (4728 Meadowlark dr Silver spring, MD 20731)
Register online www.valmontekickers.example
-passing
-kicking
-shooting
-dribbling
-ball Control
Registration :$210 (includes 1st month, registration, practice Uniform
after 1st month.

Call us Phone:(240)555-0187

• kids playing soccer , soccer fields

```html
<!DOCTYPE html>
<html lang="en">
<head>
<meta charset="utf-8">
<title>Valmonte Kickers Academy – Recreational &amp; Travel Teams</title>
<link rel="stylesheet" href="https://fonts.googleapis.com/css2?family=Montserrat:ital,wght@0,500;0,700;0,800;1,800;1,900&display=swap">
<style>
  :root {
    --page: #d8d9db;
    --navy: #0f4f9a;
    --royal: #1a3fa6;
    --sky: #2f9bdc;
    --magenta: #d02a9c;
    --lime: #c9e04a;
    --ink: #141414;
    --white: #ffffff;
    --grass-light: #c6de55;
    --grass: #5fa52a;
  }
  * { margin: 0; padding: 0; box-sizing: border-box; }
  html, body { width: 1200px; height: 1200px; overflow: hidden; }
  body {
    background: var(--page);
    font-family: "Montserrat", Arial, sans-serif;
    position: relative;
  }
  .flyer {
    position: absolute;
    left: 210px; top: 100px;
    width: 780px; height: 1000px;
    overflow: hidden;
    background: var(--white);
  }
  .flyer__photo {
    position: absolute; inset: 0;
    background:
      radial-gradient(ellipse 260px 340px at 250px 300px, rgba(40,90,200,0.35), transparent 70%),
      linear-gradient(180deg, #f3f1e8 0%, #eef0df 28%, #d3e58a 48%, var(--grass-light) 62%, #8cc43b 80%, var(--grass) 100%);
  }
  .flyer__shapes { position: absolute; inset: 0; width: 780px; height: 1000px; }

  .brand {
    position: absolute; left: 500px; top: 100px; width: 260px;
    display: flex; align-items: center; justify-content: center; gap: 12px;
  }
  .brand__dot { width: 34px; height: 34px; border-radius: 50%; background: var(--white); flex: none; }
  .brand__name { color: var(--white); font-weight: 800; font-size: 24px; line-height: 1.1; }

  .skills { position: absolute; left: 0; top: 272px; list-style: none; }
  .skills__item {
    width: 196px; margin-bottom: 16px;
    background: var(--sky);
    clip-path: polygon(0 0, 100% 0, 92% 100%, 0 100%);
    color: var(--white); font-weight: 900; font-style: italic;
    font-size: 19px; line-height: 1.05; padding: 8px 0 8px 26px;
    position: relative; text-transform: uppercase;
  }
  .skills__item::before {
    content: "▸"; position: absolute; left: 10px; top: 8px; font-style: normal; font-size: 15px;
  }

  .headline {
    position: absolute; right: 22px; top: 462px; text-align: right;
    font-weight: 900; font-style: italic; line-height: 1;
  }
  .headline__top {
    display: block; font-size: 56px; color: var(--sky);
    text-shadow: 0 0 2px var(--white), 0 0 4px var(--white), 2px 3px 5px rgba(0,0,0,.25);
  }
  .headline__bottom {
    display: block; font-size: 43px; color: var(--royal); margin-top: 4px;
    text-shadow: 0 0 3px var(--white), 0 0 6px var(--white);
  }

  .details {
    position: absolute; left: 192px; top: 614px;
    font-size: 20px; color: var(--ink); font-weight: 500; line-height: 27px;
  }
  .details__label { font-weight: 800; }
  .details__indent { padding-left: 82px; }

  .register {
    position: absolute; left: 400px; top: 720px; width: 380px; height: 66px;
    background: var(--navy);
    clip-path: polygon(40px 0, 100% 0, 100% 100%, 40px 100%, 0 50%);
    color: var(--white); font-weight: 900; font-style: italic; font-size: 32px;
    display: flex; align-items: center; justify-content: flex-end; padding-right: 22px;
  }

  .contact {
    position: absolute; right: 16px; top: 800px; text-align: right;
    color: var(--white); font-weight: 800; line-height: 1.05;
    text-shadow: 0 1px 3px rgba(0,0,0,.35);
  }
  .contact__web, .contact__call { font-size: 23px; }
  .contact__phone { font-size: 30px; margin-top: 8px; }

  .price {
    position: absolute; left: 36px; top: 754px; width: 210px; text-align: center;
    color: var(--white); font-weight: 900; font-style: italic; font-size: 62px;
    text-shadow: 2px 3px 4px rgba(0,0,0,.35);
  }

  .includes {
    position: absolute; left: 22px; top: 930px;
    color: var(--white); font-weight: 700; font-size: 21px; line-height: 30px;
  }
  .includes__label, .includes__tick { color: var(--lime); }
</style>
</head>
<body>
  <main class="flyer">
    <div class="flyer__photo" role="img" aria-label="Photo of a cheerful young player in a blue shirt holding a soccer ball above his head in front of a goal net on a grass field"></div>

    <svg class="flyer__shapes" viewBox="0 0 780 1000" aria-hidden="true">
      <defs>
        <linearGradient id="panel-fade" x1="0" y1="0" x2="0" y2="1">
          <stop offset="0" stop-color="#ffffff"/>
          <stop offset="0.55" stop-color="#ffffff" stop-opacity="0.85"/>
          <stop offset="1" stop-color="#ffffff" stop-opacity="0"/>
        </linearGradient>
      </defs>
      <path d="M420,0 H780 V330 C700,345 610,330 560,280 C500,220 455,120 420,0 Z" fill="#e9ecef"/>
      <path d="M440,0 H780 V310 C700,322 620,310 575,265 C520,210 475,115 440,0 Z" fill="var(--navy)"/>
      <path d="M0,600 C200,430 460,345 780,345 V740 H0 Z" fill="url(#panel-fade)"/>
      <path d="M0,560 C180,400 450,305 780,300 V345 C460,345 200,430 0,610 Z" fill="var(--navy)"/>
      <path d="M0,720 C60,705 120,690 170,680 L0,800 Z" fill="var(--navy)"/>
      <path d="M0,865 C220,855 500,890 690,1000 H0 Z" fill="#eef1f4"/>
      <path d="M0,885 C220,878 480,905 650,1000 H0 Z" fill="var(--navy)"/>
      <g transform="translate(141,791)" fill="var(--white)">
        <rect x="-88" y="-88" width="176" height="176"/>
        <rect x="-88" y="-88" width="176" height="176" transform="rotate(22.5)"/>
        <rect x="-88" y="-88" width="176" height="176" transform="rotate(45)"/>
        <rect x="-88" y="-88" width="176" height="176" transform="rotate(67.5)"/>
      </g>
      <g transform="translate(141,791)" fill="var(--magenta)">
        <rect x="-80" y="-80" width="160" height="160"/>
        <rect x="-80" y="-80" width="160" height="160" transform="rotate(22.5)"/>
        <rect x="-80" y="-80" width="160" height="160" transform="rotate(45)"/>
        <rect x="-80" y="-80" width="160" height="160" transform="rotate(67.5)"/>
      </g>
      <polyline points="408,724 380,753 408,782" fill="none" stroke="var(--navy)" stroke-width="8"/>
    </svg>

    <div class="brand">
      <span class="brand__dot"></span>
      <span class="brand__name">Valmonte Kickers Academy</span>
    </div>

    <ul class="skills">
      <li class="skills__item">Passing</li>
      <li class="skills__item">Kicking</li>
      <li class="skills__item">Shooting</li>
      <li class="skills__item">Dribbling</li>
      <li class="skills__item">Ball<br>Control</li>
    </ul>

    <h1 class="headline">
      <span class="headline__top">Recreational</span>
      <span class="headline__bottom">&amp; Travel Teams</span>
    </h1>

    <div class="details">
      <p><span class="details__label">AGES :</span> 5 to 14 years old</p>
      <p><span class="details__label">FIELD:</span> Holloway Fenwick Middle School</p>
      <p class="details__indent">(4728 Meadowlark dr Silver spring, MD 20731)</p>
    </div>

    <div class="register">Register ONLINE</div>

    <div class="contact">
      <p class="contact__web">www.valmontekickers.example</p>
      <p class="contact__call">OR CALL US:</p>
      <p class="contact__phone">(240)555-0187</p>
    </div>

    <p class="price">$210</p>

    <div class="includes">
      <p><span class="includes__label">INCLUDES:</span> <span class="includes__tick">✓</span> 1st month <span class="includes__tick">✓</span> Registration</p>
      <p><span class="includes__tick">✓</span> Practice <span class="includes__tick">✓</span> Uniform after 1st month</p>
    </div>
  </main>
</body>
</html>
```